New custom software business needs a Wordpress site

We need a Wordpress site for a new company based out of Chicago called 'Vellora Consulting'. Using a mix of on and off-shore resources we build custom software solutions, mainly focusing on small to medium sized companies. We help our customers "aspire" to do great things.
We have a basic site up here: https://brindlewave.example/. We worked on the content for it but not the branding. For now, this houses all the pages (except for a Contact Us page we'll be adding soon) for the foreseeable future.
We also have a new logo (attached) that we'd like to base the styling/colors on.
Target Market(s)
Small to medium sized companies that require tech resources
Industry/Entity Type
Software
Nice to have
- Teamwork, tech, professional but not elitist

```html
<!DOCTYPE html>
<html lang="en">
<head>
<meta charset="utf-8">
<title>Vellora Consulting</title>
<link rel="stylesheet" href="https://fonts.googleapis.com/css2?family=Poppins:ital,wght@0,400;0,500;0,600;0,700;1,400&display=swap">
<style>
:root{
  --blue:#1a6fd6;
  --blue-deep:#0f4fb0;
  --ink:#1f3350;
  --text:#3e4a5c;
  --muted:#8a94a3;
  --pale:#dfeafa;
  --pale-2:#eef4fc;
  --navy:#123b7f;
  --navy-2:#1a4a9e;
  --star:#f5b50a;
  --white:#fff;
}
*{box-sizing:border-box;margin:0;padding:0}
html,body{width:1200px;height:4777px;overflow:hidden}
body{font-family:"Poppins",sans-serif;color:var(--text);background:var(--white);position:relative}
section,header,footer{position:relative;width:1200px;overflow:hidden}
.abs{position:absolute}
h2{font-family:"Poppins",sans-serif;font-weight:600;color:var(--ink);font-size:40px;letter-spacing:1px;line-height:1.1}
.btn{position:absolute;display:inline-block;background:var(--blue);color:#fff;font-size:13px;text-transform:uppercase;padding:0 20px;height:34px;line-height:34px;letter-spacing:.3px}
.btn::after{content:"";position:absolute;right:0;top:0;border-top:14px solid var(--navy);border-left:14px solid transparent}
.photo{position:absolute}

/* hero */
.hero{height:649px;background:linear-gradient(135deg,#f4f8fd 0%,#fff 45%)}
.hero .band{position:absolute;left:0;top:0;width:260px;height:649px;background:linear-gradient(160deg,#e3edfa,#f6f9fe);clip-path:polygon(0 0,100% 0,0 100%)}
.hero .band-2{position:absolute;left:0;top:480px;width:150px;height:169px;background:#e6effb;clip-path:polygon(100% 0,100% 0,0 100%,0 60%)}
.nav{position:absolute;left:150px;top:30px;width:960px;height:76px;background:#fff;box-shadow:0 6px 24px rgba(30,60,110,.08);clip-path:polygon(0 0,100% 0,95% 100%,0 100%);z-index:2}
.brand{position:absolute;left:28px;top:22px;display:flex;align-items:center;gap:10px;font-weight:600;font-size:20px;color:var(--blue);letter-spacing:1px}
.brand i{display:block;width:26px;height:26px;background:var(--blue)}
.nav ul{position:absolute;left:222px;top:28px;display:flex;list-style:none;font-size:14px;color:var(--ink)}
.nav li{margin-right:28px}
.nav li.on{color:var(--blue);position:relative}
.call{position:absolute;left:753px;top:22px;width:128px;height:36px;line-height:36px;text-align:center;background:var(--blue);color:#fff;font-size:14px}
.nav-mark{position:absolute;left:378px;top:100px;width:30px;height:6px;background:var(--blue);transform:skewX(-30deg);z-index:3}
.hero h1{position:absolute;left:174px;top:210px;font-size:46px;line-height:1.12;font-weight:600;color:var(--navy);letter-spacing:1.5px}
.hero p{position:absolute;left:174px;top:324px;width:300px;font-size:14.5px;line-height:1.6;color:var(--ink)}
.hero .btn{left:174px;top:423px}
.dots{position:absolute;left:170px;top:550px;display:flex;gap:6px}
.dots span{width:28px;height:6px;background:#c9d3df;transform:skewX(-30deg)}
.dots span.on{background:var(--blue)}
.hero .photo{left:380px;top:106px;width:820px;height:543px;background:linear-gradient(120deg,#4a3c33 0%,#a59a90 45%,#e6ebee 75%,#cdd6de 100%);clip-path:polygon(28% 0,100% 0,100% 100%,0 100%,0 82%)}

/* about */
.about{height:672px}
.about .photo{left:6px;top:111px;width:588px;height:446px;background:linear-gradient(135deg,#d9b79c,#a57c5f 40%,#6f8fb8 70%,#d8e2ef)}
.about .photo.a{clip-path:polygon(40% 0,100% 0,60% 100%,0 100%)}
.about .photo.b{left:140px;clip-path:polygon(63% 0,75% 0,40% 100%,28% 100%);background:#fff;opacity:.9}
.about h2{position:absolute;left:649px;top:128px}
.about .copy{position:absolute;left:649px;top:200px;width:380px;font-size:13.5px;line-height:1.67}
.about .copy p+p{margin-top:10px}
.about .btn{left:649px;top:514px}

/* services */
.services{height:471px;background:var(--pale)}
.services h2{text-align:center;width:100%;position:absolute;top:92px}
.svc{position:absolute;top:185px;width:420px;height:171px;background:#fff;display:flex;box-shadow:0 8px 24px rgba(20,60,120,.08)}
.svc .ico{flex:none;width:110px;height:171px;background:var(--blue-deep);clip-path:polygon(0 0,100% 0,80% 100%,0 100%);display:flex;align-items:center;justify-content:center;padding-right:20px}
.svc .body{padding:22px 26px 0 14px;width:310px}
.svc h3{font-size:14.5px;font-weight:500;color:var(--ink);letter-spacing:.4px;margin-bottom:8px}
.svc p{font-size:12px;line-height:1.63;color:var(--muted)}
.svc a{display:block;margin-top:10px;font-size:13px;color:var(--blue);text-decoration:none}
.svc::after{content:"";position:absolute;right:0;top:0;width:22px;height:171px;background:var(--blue-deep);clip-path:polygon(100% 0,100% 100%,0 100%)}
.svc.one{left:174px}.svc.two{left:605px}

/* why */
.why{height:735px}
.why h2{position:absolute;left:174px;top:105px}
.why ul{position:absolute;left:174px;top:195px;list-style:none;width:390px}
.why li{display:flex;gap:16px;font-size:13.5px;line-height:1.68;margin-bottom:20px}
.why li svg{flex:none;margin-top:4px}
.why .btn{left:174px;top:590px}
.why .photo.bg{left:588px;top:180px;width:592px;height:360px;background:linear-gradient(135deg,#e8eef4,#b8c3cc 55%,#d4dde4);clip-path:polygon(0 0,40% 0,100% 100%,20% 100%)}
.why .photo.fg{left:745px;top:91px;width:375px;height:538px;background:linear-gradient(180deg,#e2e6ea 0%,#2c3340 40%,#1a1f28 100%);clip-path:polygon(30% 0,75% 0,100% 100%,0 100%)}

/* leadership */
.lead{height:534px;background:var(--blue)}
.lead h2{color:#fff;text-align:center;position:absolute;width:100%;top:114px}
.card{position:absolute;top:237px;width:420px;height:173px;background:#fff;display:flex}
.card .photo{position:relative;flex:none;width:200px;height:173px;background:linear-gradient(180deg,#dfe6ee,#33435c 60%,#22304a)}
.card .body{padding:16px 12px 0 20px;width:220px}
.card h3{font-size:17px;font-weight:500;color:var(--blue)}
.card .role{font-size:12px;font-style:italic;color:var(--muted)}
.card .soc{display:flex;gap:10px;margin:6px 0 8px}
.card .soc i{width:18px;height:18px;border-radius:50%;background:var(--blue);display:block}
.card p{font-size:11.5px;line-height:1.65;color:var(--ink)}
.card.one{left:174px}.card.two{left:607px}

/* testimonials */
.testi{height:556px}
.testi h2{text-align:center;position:absolute;width:100%;top:124px}
.tcard{position:absolute;top:273px;width:401px;height:232px;background:#fff;box-shadow:0 4px 20px rgba(20,40,80,.12);text-align:center}
.avatar{position:absolute;top:-34px;left:50%;margin-left:-32px;width:64px;height:64px;border-radius:50%;background:linear-gradient(#9aa5b3,#4e5968);border:3px solid #fff}
.tcard h3{margin-top:40px;font-size:17px;font-weight:500;color:var(--blue)}
.stars{color:var(--star);font-size:22px;letter-spacing:7px;margin-top:2px}
.tcard p{font-size:13px;font-style:italic;line-height:1.75;color:var(--text);padding:0 28px;margin-top:10px}
.tcard.one{left:176px}.tcard.two{left:623px}
.arrow{position:absolute;top:3375px;width:28px;height:28px;background:var(--pale);color:var(--blue);font-size:14px;line-height:28px;text-align:center;border-radius:4px}

/* contact */
.contact{height:690px;background:var(--pale-2)}
.contact h2{position:absolute;left:174px;top:123px}
.field{position:absolute;left:174px;width:420px;height:56px;background:#fff;border:1px solid #d6dde7;font-size:13px;color:var(--muted);padding:18px 22px;display:flex;justify-content:space-between}
.field.msg{height:118px;align-items:flex-start}
.contact .btn{left:174px;top:546px}
.map-wrap{position:absolute;left:644px;top:149px;width:380px;height:400px}
.map-wrap::before{content:"";position:absolute;right:0;bottom:0;width:250px;height:220px;background:var(--blue)}
.map{position:absolute;left:0;top:0;width:364px;height:383px;background:linear-gradient(135deg,#eef1f3,#dfe5e8 50%,#c9d8cf)}
.pin{position:absolute;left:145px;top:135px}

/* footer */
.foot{height:392px;background:var(--navy);color:#d7e2f4}
.foot .brand{left:174px;top:80px;color:#fff;font-size:30px;font-weight:500}
.foot .brand i{width:44px;height:44px;background:#fff}
.foot .about-f{position:absolute;left:174px;top:193px;width:310px;font-size:14px;line-height:1.6}
.foot h4{position:absolute;top:80px;font-size:16px;font-weight:500;color:#fff}
.foot .links{position:absolute;left:569px;top:135px;list-style:none;font-size:14px;line-height:30.5px}
.info{position:absolute;left:811px;display:flex;align-items:center;gap:18px;font-size:14px}
.info i{width:38px;height:38px;background:#fff;display:flex;align-items:center;justify-content:center}
.foot .soc{position:absolute;left:814px;top:278px;display:flex;gap:22px}
.foot .soc i{width:34px;height:34px;border-radius:50%;background:#fff;display:block}
.copy-strip{height:78px;background:var(--navy-2);color:#b9c8e3;font-size:13px;text-align:center;line-height:78px}
.copy-strip span{color:#4fa0ff}
</style>
</head>
<body>

<header class="hero">
  <div class="band"></div><div class="band-2"></div>
  <div class="photo" role="img" aria-label="Photo of two businessmen talking across a table with laptops in a bright office"></div>
  <nav class="nav">
    <div class="brand"><i></i>VELLORA</div>
    <ul><li class="on">Home</li><li>About</li><li>Why Vellora?</li><li>Services</li><li>Leadership</li><li>Contact</li></ul>
    <div class="call">Call Now</div>
  </nav>
  <div class="nav-mark"></div>
  <h1>VELLORA<br>CONSULTING</h1>
  <p>Welcome to Vellora, a software consulting company specializing in serving small to medium size businesses.</p>
  <span class="btn">Get Started</span>
  <div class="dots"><span></span><span class="on"></span><span></span></div>
</header>

<section class="about">
  <div class="photo a" role="img" aria-label="Photo of a smiling team gathered around a laptop"></div>
  <div class="photo b"></div>
  <h2>ABOUT VELLORA</h2>
  <div class="copy">
    <p>Welcome to Vellora, a software consulting company specializing in serving small to medium size businesses. We understand the unique challenges and opportunities that these companies face, and we are dedicated to helping them succeed through innovative technology solutions.</p>
    <p>Our team of experienced professionals has a diverse range of skills and expertise, making us well-equipped to handle any project, big or small. We specialize in custom software development, working closely with our clients to understand their specific needs and build solutions that meet their requirements.</p>
  </div>
  <span class="btn">Learn More</span>
</section>

<section class="services">
  <h2>OUR SERVICES</h2>
  <div class="svc one">
    <div class="ico"><svg width="54" height="54" viewBox="0 0 54 54" fill="none" stroke="#fff" stroke-width="2"><circle cx="27" cy="22" r="13"/><path d="M21 38h12M23 44h8M20 22h14M27 15v14"/></svg></div>
    <div class="body"><h3>CUSTOM SOLUTION DELIVERY</h3><p>Vellora offers a range of services focused on helping businesses and organizations deliver software solutions to their customers or users.</p><a>Learn More &rarr;</a></div>
  </div>
  <div class="svc two">
    <div class="ico"><svg width="54" height="54" viewBox="0 0 54 54" fill="none" stroke="#fff" stroke-width="2"><rect x="16" y="6" width="22" height="42" rx="3"/><path d="M27 18l8 4v8l-8 4-8-4v-8zM19 22l8 4 8-4M27 26v8"/></svg></div>
    <div class="body"><h3>STAFF AUGMENTATION</h3><p>Vellora offers a range of services focused on helping businesses and organizations deliver software solutions to their customers or users.</p><a>Learn More &rarr;</a></div>
  </div>
</section>

<section class="why">
  <h2>WHY VELLORA?</h2>
  <ul>
    <li><svg width="56" height="52" viewBox="0 0 56 52" fill="none" stroke="#1a6fd6" stroke-width="2"><circle cx="28" cy="14" r="7"/><path d="M6 30c6 10 14 16 22 16s16-6 22-16"/></svg><span>Welcome to Vellora, a software consulting company specializing in serving small to medium size businesses.</span></li>
    <li><svg width="56" height="52" viewBox="0 0 56 52" fill="none" stroke="#1a6fd6" stroke-width="2"><circle cx="14" cy="22" r="5"/><circle cx="28" cy="16" r="5"/><circle cx="42" cy="22" r="5"/><path d="M6 40c0-6 16-6 16 0M20 34c0-6 16-6 16 0M34 40c0-6 16-6 16 0"/></svg><span>We understand that delivering a high-quality software solution requires more than just technical expertise.</span></li>
    <li><svg width="56" height="52" viewBox="0 0 56 52" fill="none" stroke="#1a6fd6" stroke-width="2"><rect x="6" y="20" width="30" height="22"/><path d="M36 26h10l4 6v10H36M14 42v4M42 42v4"/></svg><span>Our team members are committed to delivering excellence in everything they do, and they are always looking for ways to improve processes and drive results.</span></li>
    <li><svg width="56" height="52" viewBox="0 0 56 52" fill="none" stroke="#1a6fd6" stroke-width="2"><circle cx="34" cy="14" r="9"/><path d="M29 14l4 4 6-7M6 40l10-6h14l12-6"/></svg><span>If you are in need of IT professionals who understand what it takes to deliver a quality solution, we encourage you to contact</span></li>
  </ul>
  <span class="btn">Learn More</span>
  <div class="photo bg" role="img" aria-label="Photo of an open-plan office with staff at desks"></div>
  <div class="photo fg" role="img" aria-label="Photo of a smiling consultant in a dark suit pointing to the side"></div>
</section>

<section class="lead">
  <h2>VELLORA LEADERSHIP</h2>
  <div class="card one">
    <div class="photo" role="img" aria-label="Portrait of Dario Kessel in a suit holding a tablet"></div>
    <div class="body"><h3>Dario Kessel</h3><div class="role">leader</div><div class="soc"><i></i><i></i><i></i></div><p>As a leader, Dario is dedicated to fostering a culture of collaboration, innovation, and</p></div>
  </div>
  <div class="card two">
    <div class="photo" role="img" aria-label="Portrait of Tomas Reyne in a suit with arms crossed"></div>
    <div class="body"><h3>Tomas Reyne</h3><div class="role">leader</div><div class="soc"><i></i><i></i><i></i></div><p>As a leader, Tomas is dedicated to fostering a culture of collaboration, innovation, and</p></div>
  </div>
</section>

<section class="testi">
  <h2>TESTIMONIALS</h2>
  <div class="tcard one"><div class="avatar" role="img" aria-label="Portrait of Lena Marsh"></div><h3>Lena Marsh</h3><div class="stars">★★★★★</div><p>“Lorem ipsum dolor sit amet, consectetur adipiscing elit, sed do eiusmod tempor incididunt ut labore et dolore magna aliqua. Ut enim ad minim veniam, quis nostrud exercitation ullamco”</p></div>
  <div class="tcard two"><div class="avatar" role="img" aria-label="Portrait of Idris Kalvo"></div><h3>Idris Kalvo</h3><div class="stars">★★★★★</div><p>“Lorem ipsum dolor sit amet, consectetur adipiscing elit, sed do eiusmod tempor incididunt ut labore et dolore magna aliqua. Ut enim ad minim veniam, quis nostrud exercitation ullamco”</p></div>
</section>
<div class="arrow" style="left:126px">&larr;</div>
<div class="arrow" style="left:1056px">&rarr;</div>

<section class="contact">
  <h2>GET IN TOUCH</h2>
  <div class="field" style="top:192px"><span>Enter Your Name</span><span>&#128100;&#xFE0E;</span></div>
  <div class="field" style="top:262px"><span>Enter Your Email</span><span>&#9993;&#xFE0E;</span></div>
  <div class="field" style="top:332px"><span>Enter Your Phone</span><span>&#9742;&#xFE0E;</span></div>
  <div class="field msg" style="top:402px"><span>Enter Your Message</span><span>&#9998;&#xFE0E;</span></div>
  <span class="btn">Submit</span>
  <div class="map-wrap">
    <div class="map" role="img" aria-label="Street map of the office location"></div>
    <svg class="pin" width="40" height="52" viewBox="0 0 40 52"><path d="M20 2C10 2 2 10 2 20c0 13 18 30 18 30s18-17 18-30C38 10 30 2 20 2z" fill="#1a6fd6"/><circle cx="20" cy="20" r="7" fill="#fff"/></svg>
  </div>
</section>

<footer class="foot">
  <div class="brand abs"><i></i>VELLORA</div>
  <p class="about-f">Dario is a strong believer in the importance of continuous learning and development, and he is committed to providing his team with the resources and support they need to grow and succeed.</p>
  <h4 style="left:569px">Quick Links</h4>
  <ul class="links"><li>Home</li><li>About</li><li>Why Vellora?</li><li>Services</li><li>Leadership</li><li>Contact</li></ul>
  <h4 style="left:811px">Contact Info</h4>
  <div class="info" style="top:140px"><i><svg width="16" height="16" viewBox="0 0 16 16"><path d="M3 1l3 3-2 2c1 2 3 4 5 5l2-2 3 3-2 3C6 15 1 10 1 3z" fill="#1a6fd6"/></svg></i>+1 312 555 0148</div>
  <div class="info" style="top:197px"><i><svg width="18" height="14" viewBox="0 0 18 14"><rect x="1" y="1" width="16" height="12" fill="none" stroke="#1a6fd6" stroke-width="2"/><path d="M1 1l8 7 8-7" fill="none" stroke="#1a6fd6" stroke-width="2"/></svg></i>hello@vellora.example</div>
  <div class="soc"><i></i><i></i><i></i></div>
</footer>
<div class="copy-strip">All content © Copyright 2022 <span>Vellora</span>. All rights reserved.</div>

</body>
</html>
```